Design for three pages of a 12-page 4-color 8.5 x 11 magazine-type booklet

We will be taking the information from a webpage at quillmerefound.org and putting it into a 12-page 4-color 8.5 x 11 magazine-type booklet that will look like an upscale company report. I need to have a design in Photoshop for the cover and two inside pages that I can use as the template for the pages. I likely will also need help putting it together once I start putting the contents into the pages. I may just decide on the content and have the designer create the booklet as an additional freelance contract. First, I need a design for (1) the front cover, (2) one information page taken from information on http://www.quillmerefound.org/qbf-project-management-staff/, and (3) one of the pages that has a researcher from this page on it: http://www.quillmerefound.org/teaching-people-how-to-have/. That's designs for three pages. The designs have to be very professional looking and businesslike. We will be using the booklet to pitch to foundations and philanthropists. The work on the publication itself would be additional freelance work on an hourly basis.

Font styles to use
Serif

Colors

Designer to choose colors to be used in the design.

Requirements
Must have
• Professional look

```html
<!DOCTYPE html>
<html lang="en">
<head>
<meta charset="utf-8">
<title>Quillmere Bridge Foundation — Booklet Pages</title>
<link href="https://fonts.googleapis.com/css2?family=Merriweather:ital,wght@0,300;0,400;0,700;0,900;1,400;1,700&family=Open+Sans:wght@400;600;700&display=swap" rel="stylesheet">
<style>
:root{
  --navy:#2c2a88;
  --royal:#3d3aa8;
  --ink:#2a2a3a;
  --muted:#55586a;
  --steel:#a7a9b8;
  --silver:#d9dbe4;
  --paper:#ffffff;
  --sky-top:#c9d8ec;
  --sky-mid:#eef3fa;
  --gold:#f2b500;
  --backdrop:#e9e9ec;
  --row-a:#ffffff;
  --row-b:#eef0f7;
}
*{box-sizing:border-box;margin:0;padding:0}
html,body{width:1200px;height:3067px;overflow:hidden;background:var(--backdrop)}
body{font-family:"Merriweather",Georgia,serif;color:var(--ink);position:relative}
.spread{position:absolute;left:96px;width:1008px;height:960px;display:flex;box-shadow:0 6px 18px rgba(0,0,0,.22)}
.spread--cover{top:24px}
.spread--staff{top:1056px}
.spread--research{top:2076px}
.page{position:relative;width:504px;height:960px;background:var(--paper);overflow:hidden}
.page + .page{border-left:1px solid #e3e4ea}
.sky{position:absolute;inset:0;background:linear-gradient(180deg,var(--sky-top) 0%,var(--sky-mid) 45%,#f7f9fd 70%,var(--sky-top) 100%)}
.swoosh{position:absolute;inset:0;width:504px;height:960px}
.content{position:absolute;z-index:2}
.brand{font-family:"Merriweather",Georgia,serif;font-weight:900;color:var(--navy);letter-spacing:2px}
.page-num{position:absolute;z-index:2;font-family:"Open Sans",Arial,sans-serif;font-weight:400;color:#fff;font-size:34px;letter-spacing:2px}
/* cover */
.back-brand{position:absolute;z-index:2;left:80px;top:470px;font-size:60px}
.contact{position:absolute;z-index:2;left:80px;top:560px;list-style:none;font-family:"Open Sans",Arial,sans-serif;font-size:13px;color:var(--ink)}
.contact li{display:flex;align-items:center;gap:10px;margin-bottom:12px}
.contact svg{width:20px;height:20px;flex:none}
.front-brand{position:absolute;z-index:2;right:40px;top:120px;text-align:center;width:330px}
.front-brand .brand{font-size:74px;line-height:1}
.front-brand .legal{font-size:11px;font-weight:700;color:var(--navy);letter-spacing:.3px;margin-top:8px}
.stairs{position:absolute;left:130px;top:220px;width:250px;height:420px;background:radial-gradient(ellipse at 50% 30%,#ffffff 0%,#dfe7f3 55%,rgba(223,231,243,0) 75%)}
.cover-title{position:absolute;z-index:2;right:26px;top:700px;width:220px;color:#fff}
.cover-title h1{font-size:31px;font-weight:400;line-height:1.25}
.cover-title p{font-size:10.5px;line-height:1.55;margin-top:16px;font-weight:300}
/* headings */
.section-title{font-weight:400;color:var(--navy);font-size:28px;line-height:1.2;z-index:2}
.staff-title{position:absolute;top:170px;left:0;right:0;text-align:center}
.board-title{position:absolute;top:46px;right:28px;text-align:right}
/* staff cards */
.staff-grid{position:absolute;z-index:2;left:36px;top:290px;width:432px;display:grid;grid-template-columns:repeat(3,132px);column-gap:18px;row-gap:34px}
.card{border-right:1px solid var(--silver);padding-right:6px}
.card .role{background:var(--navy);color:#fff;font-family:"Open Sans",Arial,sans-serif;font-size:9.5px;text-align:center;padding:3px 0;border-radius:8px 8px 0 0}
.photo{background:linear-gradient(160deg,#8a7a6a,#4d4550);display:block}
.card .photo{width:126px;height:112px}
.person{font-weight:700;font-style:italic;font-size:14px;line-height:1.2;margin-top:10px;color:var(--ink)}
.person small{display:block;font-style:normal;font-weight:400;font-size:10px}
.bio{font-family:"Open Sans",Arial,sans-serif;font-size:7.5px;line-height:1.45;color:var(--muted);margin-top:6px}
/* advisory */
.board{position:absolute;z-index:2;width:140px}
.board .photo{width:140px;height:128px}
.board .bar{width:34px;height:3px;background:var(--gold);margin-top:8px}
/* research page */
.lead-photo{position:absolute;z-index:2;left:12px;top:22px;width:188px;height:178px;background:linear-gradient(160deg,#6b4a32,#3a2a28)}
.lead-bio{position:absolute;z-index:2;left:12px;top:212px;width:188px;font-size:9px;line-height:1.5;font-weight:300}
.lead-bio p + p{margin-top:10px}
.col{position:absolute;z-index:2;font-size:9px;line-height:1.5;font-weight:300}
.col h2{font-size:18px;font-weight:400;color:var(--navy);line-height:1.2;margin-bottom:6px}
.col h3{font-size:10.5px;font-weight:700;margin:12px 0 6px}
.col p + p{margin-top:9px}
.checks{list-style:none}
.checks li{display:flex;gap:8px;margin-bottom:10px;align-items:flex-start}
.checks svg{width:14px;height:14px;flex:none;margin-top:1px}
.timeline{background:var(--navy);color:#fff;font-size:16px;text-align:center;padding:12px 0;border-radius:10px 10px 0 0}
.costs{width:100%;border-collapse:collapse;font-family:"Open Sans",Arial,sans-serif;font-size:9.5px}
.costs caption{text-align:left;font-family:"Merriweather",Georgia,serif;font-size:16px;color:var(--navy);padding:14px 0 6px}
.costs td{padding:4px 6px;border-bottom:1px solid var(--silver)}
.costs tr:nth-child(odd) td{background:var(--row-a)}
.costs tr:nth-child(even) td{background:var(--row-b)}
.costs td:last-child{text-align:left;width:38%}
.costs tr.total td{background:var(--navy);color:#fff;font-weight:700}
</style>
</head>
<body>

<!-- Spread 1: back and front cover -->
<section class="spread spread--cover">
  <article class="page page--back">
    <div class="sky" role="img" aria-label="Soft sky of white clouds"></div>
    <svg class="swoosh" viewBox="0 0 504 960" aria-hidden="true">
      <path d="M0 0H360C280 70 140 150 0 210Z" fill="var(--navy)"/>
      <path d="M0 210C140 150 280 70 360 0H390C300 80 150 165 0 232Z" fill="var(--steel)"/>
      <path d="M0 232C150 165 300 80 390 0H402C310 86 160 175 0 246Z" fill="#fff"/>
      <path d="M504 960V690C410 800 260 900 110 960Z" fill="var(--navy)"/>
      <path d="M504 690C410 800 260 900 110 960H80C240 890 400 790 504 660Z" fill="var(--steel)"/>
    </svg>
    <div class="back-brand brand">QBF</div>
    <ul class="contact">
      <li><svg viewBox="0 0 20 20"><rect width="20" height="20" rx="3" fill="var(--navy)"/><path d="M6 4l2 3-1.2 1.4a8 8 0 0 0 4.8 4.8L13 12l3 2-1 2.4C9 16 4 11 3.6 5z" fill="#fff"/></svg>800-555-0147, 309-555-0183</li>
      <li><svg viewBox="0 0 20 20"><rect width="20" height="20" rx="3" fill="var(--navy)"/><rect x="4" y="6" width="12" height="8" fill="none" stroke="#fff" stroke-width="1.4"/><path d="M4 6l6 5 6-5" fill="none" stroke="#fff" stroke-width="1.4"/></svg>information@quillmerestudies.org</li>
      <li><svg viewBox="0 0 20 20"><rect width="20" height="20" rx="3" fill="var(--navy)"/><path d="M10 3a5 5 0 0 1 5 5c0 4-5 9-5 9S5 12 5 8a5 5 0 0 1 5-5z" fill="#fff"/><circle cx="10" cy="8" r="1.8" fill="var(--navy)"/></svg>48 Harlow Lane, Brookfield, IL 61790</li>
      <li><svg viewBox="0 0 20 20"><rect width="20" height="20" rx="3" fill="var(--navy)"/><circle cx="10" cy="10" r="5.5" fill="none" stroke="#fff" stroke-width="1.3"/><path d="M4.5 10h11M10 4.5c-3 3-3 8 0 11M10 4.5c3 3 3 8 0 11" fill="none" stroke="#fff" stroke-width="1"/></svg>www.quillmerefound.org</li>
    </ul>
  </article>

  <article class="page page--front">
    <div class="sky" role="img" aria-label="Soft sky of white clouds"></div>
    <div class="stairs" role="img" aria-label="Staircase rising into bright clouds"></div>
    <svg class="swoosh" viewBox="0 0 504 960" aria-hidden="true">
      <path d="M504 0V70C470 40 440 20 410 0Z" fill="var(--navy)"/>
      <path d="M0 960V780C170 730 360 630 504 470V960Z" fill="var(--navy)"/>
      <path d="M0 780C170 730 360 630 504 470V445C360 605 170 705 0 755Z" fill="var(--steel)"/>
      <path d="M0 755C170 705 360 605 504 445V430C360 590 170 690 0 740Z" fill="#fff"/>
    </svg>
    <div class="front-brand">
      <div class="brand">QBF</div>
      <div class="legal">QUILLMERE BRIDGE FOUNDATION, INC.</div>
    </div>
    <div class="cover-title">
      <h1>Bridging<br>Heaven<br>and Earth</h1>
      <p>When all people realize we are eternal beings, humankind will live together in love, peace, and joy.</p>
    </div>
  </article>
</section>

<!-- Spread 2: staff and advisory board -->
<section class="spread spread--staff">
  <article class="page page--staff">
    <div class="sky" role="img" aria-label="Faint sky of white clouds" style="opacity:.45"></div>
    <svg class="swoosh" viewBox="0 0 504 960" aria-hidden="true">
      <path d="M0 0H504V20C360 60 180 100 0 150Z" fill="var(--navy)"/>
      <path d="M0 150C180 100 360 60 504 20V34C360 76 180 118 0 168Z" fill="var(--steel)"/>
      <path d="M0 960V860C120 900 250 930 380 960Z" fill="var(--navy)"/>
      <path d="M0 860C120 900 250 930 380 960H410C280 925 140 885 0 838Z" fill="var(--steel)"/>
    </svg>
    <div class="page-num" style="left:24px;top:30px">001</div>
    <h2 class="section-title staff-title">QBF Project<br>Management Staff</h2>
    <div class="staff-grid">
      <div class="card">
        <div class="role">Project Director</div>
        <div class="photo" role="img" aria-label="Portrait of the project director"></div>
        <div class="person">R. Daniel Marsh, <small>PhD</small></div>
        <p class="bio">Dr. Marsh is the president of QBF. His PhD is in supervision and counseling. He is the co-author of several books and a guide on the personal growth method.</p>
      </div>
      <div class="card">
        <div class="role">Finance</div>
        <div class="photo" role="img" aria-label="Portrait of the finance officer"></div>
        <div class="person">Lena Ashford</div>
        <p class="bio">Lena was employed for 31 years by the Department of Defense, where she was an analyst and a federal auditor and then a certified professional in finance.</p>
      </div>
      <div class="card">
        <div class="role">Administration</div>
        <div class="photo" role="img" aria-label="Portrait of the administrator"></div>
        <div class="person">Karen Whitby</div>
        <p class="bio">Karen has been CEO of an integrative medical group, vice president of operations and human resources for a state public school district.</p>
      </div>
      <div class="card">
        <div class="role">Media</div>
        <div class="photo" role="img" aria-label="Portrait of the media director"></div>
        <div class="person">Sylvia Carrow</div>
        <p class="bio">Sylvia is the founder and producer of a weekly radio show. She is the author of a popular book on grief and hope.</p>
      </div>
      <div class="card">
        <div class="role">Education</div>
        <div class="photo" role="img" aria-label="Portrait of the education director"></div>
        <div class="person">Ron Kestrel</div>
        <p class="bio">Ron is a history, civics and language arts elementary school teacher and a graduate with a BA in English and arts studies.</p>
      </div>
      <div class="card">
        <div class="role">Publications</div>
        <div class="photo" role="img" aria-label="Row of published book covers" style="background:linear-gradient(160deg,#c7a24a,#6a3b2a)"></div>
        <div class="person">Wider Horizon Press</div>
        <p class="bio">Wider Horizon Press is a wholly owned publisher that specializes in books by leading authors in afterlife studies.</p>
      </div>
    </div>
  </article>

  <article class="page page--board">
    <div class="sky" role="img" aria-label="Faint sky of white clouds" style="opacity:.45"></div>
    <svg class="swoosh" viewBox="0 0 504 960" aria-hidden="true">
      <path d="M504 0H380C430 25 470 45 504 60Z" fill="var(--navy)"/>
      <path d="M504 960V700C400 820 250 910 60 960Z" fill="var(--navy)"/>
      <path d="M504 700C400 820 250 910 60 960H30C230 900 390 800 504 670Z" fill="var(--steel)"/>
    </svg>
    <h2 class="section-title board-title">QBF Research<br>Advisory Board</h2>
    <div class="board" style="left:20px;top:156px">
      <div class="photo" role="img" aria-label="Portrait of a board member"></div>
      <div class="person">Alice Brandt, <small>PhD</small></div>
      <p class="bio">Dr. Brandt is the Director of Research for a national institute for life between lives and an author on the subject.</p>
      <div class="bar"></div>
    </div>
    <div class="board" style="left:182px;top:156px">
      <div class="photo" role="img" aria-label="Portrait of a board member"></div>
      <div class="person">Dana Whitfield-Orme, <small>MS</small></div>
      <p class="bio">Dana is a researcher and founder and owner of a research consultancy.</p>
      <div class="bar"></div>
    </div>
    <div class="board" style="left:344px;top:156px">
      <div class="photo" role="img" aria-label="Portrait of a board member"></div>
      <div class="person">Einar Holmgren, <small>PhD</small></div>
      <p class="bio">Dr. Holmgren has a PhD in psychology. He is Emeritus Professor of Psychology and a research associate of a society for psychical research.</p>
      <div class="bar"></div>
    </div>
    <div class="board" style="left:96px;top:470px">
      <div class="photo" role="img" aria-label="Portrait of a board member"></div>
      <div class="person">Jon Verhoeven</div>
      <p class="bio">Dr. Verhoeven was appointed to undergraduate work at a state college. He holds a PhD in physics from a university in South Africa.</p>
      <div class="bar"></div>
    </div>
    <div class="board" style="left:266px;top:470px">
      <div class="photo" role="img" aria-label="Portrait of a board member"></div>
      <div class="person">Walter Brennick, <small>MD, MPH</small></div>
      <p class="bio">Dr. Brennick is a Board Certified Occupational Medicine physician who was assistant chief at a major medical center.</p>
      <div class="bar"></div>
    </div>
    <div class="page-num" style="right:24px;top:880px">002</div>
  </article>
</section>

<!-- Spread 3: research pages -->
<section class="spread spread--research">
  <article class="page page--leader">
    <div class="sky" role="img" aria-label="Faint sky of white clouds" style="opacity:.45"></div>
    <svg class="swoosh" viewBox="0 0 504 960" aria-hidden="true">
      <path d="M0 960V760C120 850 260 920 420 960Z" fill="var(--navy)"/>
      <path d="M0 760C120 850 260 920 420 960H450C280 910 130 830 0 730Z" fill="var(--steel)"/>
    </svg>
    <div class="lead-photo" role="img" aria-label="Portrait of the foundation president"></div>
    <div class="lead-bio">
      <p>R. Daniel Marsh, president of QBF, has developed an online training program that enables anyone to connect with loved ones living on the next plane of life. It uses a form of self-hypnosis to bring the experiencer into a state in which the connections may occur. It then teaches the experiencer how to allow free, open unfoldment so messages can come through from the loved one. The experiencers fill out journals after each stage that are submitted to QBF. Dr. Marsh reads each journal and coaches experiencers to help them learn how to have an afterlife connection by allowing free unfoldment.</p>
      <p>The procedure is free on the Internet at this link: Guided Reunion Sessions</p>
    </div>
    <div class="col" style="left:218px;top:24px;width:260px">
      <h2>Successes and Validations</h2>
      <p>Approximately 80% of those who go through the stages in the training have afterlife connections. The method is named Guided Reunion Sessions. It is available through any standard Web browser on the Internet and is free. The method has now been experienced by thousands of people. We continue to evaluate and refine it to help people learn how to make their own afterlife connections with loved ones.</p>
      <p>You can read the report about the procedure and study, containing accounts of actual sessions, at this link: Read the study</p>
      <p>To read additional accounts of sessions, go to this link: Additional accounts of connections</p>
      <p>To read accounts that resulted in validations, such as when the experiencer learned things he or she could not have known that were discovered to be true, go to this link: Validations</p>
      <h2 style="margin-top:16px">Future Advancements with Funding</h2>
      <p>With funding, the model can be expanded to allow more people to learn how to have successful afterlife communication. The procedure can be refined to be even more successful. As a result, this medium will have a profound effect on many people's level of grief, their understanding of who they are in eternity, and their relationships with other people in their lives.</p>
      <h3>Funding will make possible</h3>
      <ul class="checks">
        <li><svg viewBox="0 0 14 14"><circle cx="7" cy="7" r="7" fill="var(--navy)"/><path d="M4 7.2l2 2 4-4.4" fill="none" stroke="#fff" stroke-width="1.6"/></svg>validating the procedure to demonstrate that the connections are valid connections with loved ones</li>
        <li><svg viewBox="0 0 14 14"><circle cx="7" cy="7" r="7" fill="var(--navy)"/><path d="M4 7.2l2 2 4-4.4" fill="none" stroke="#fff" stroke-width="1.6"/></svg>studying the procedure to determine how it can be refined to improve afterlife communication</li>
        <li><svg viewBox="0 0 14 14"><circle cx="7" cy="7" r="7" fill="var(--navy)"/><path d="M4 7.2l2 2 4-4.4" fill="none" stroke="#fff" stroke-width="1.6"/></svg>translating the procedures into French and Spanish</li>
      </ul>
    </div>
    <div class="page-num" style="left:24px;top:880px">003</div>
  </article>

  <article class="page page--account">
    <div class="sky" role="img" aria-label="Faint sky of white clouds" style="opacity:.45"></div>
    <svg class="swoosh" viewBox="0 0 504 960" aria-hidden="true">
      <path d="M0 0H504V110C360 60 180 20 60 0Z" fill="var(--navy)"/>
      <path d="M60 0C180 20 360 60 504 110V128C350 76 170 30 30 0Z" fill="var(--steel)"/>
      <path d="M0 960V860C150 900 300 935 440 960Z" fill="var(--navy)"/>
    </svg>
    <div class="page-num" style="right:24px;top:28px">004</div>
    <div class="col" style="left:18px;top:140px;width:226px">
      <h2>Example Account by an Experiencer</h2>
      <p>I went to the same garden (my own) and again found what I did not expect. My uncle (he talked about the same time as my father) was sitting in the seat my brother used, and my father was near the table. Both of them had been gone for many years. Uncle and I talked and he told me how much he had enjoyed the orchard, and he asked me to pick the fruit that was ripe. I had not thought of him for a long time. He began talking to me about the farm where I grew up. We walked out from the farmhouse and he began sharing about how it was when he grew up there. I had not thought of that much until he and my dad spent their childhood there. I turned to look at the ridge where I used to walk and daydream. Immediately he took both of us to the ridge. He said it was one of his favorite places too. Then he talked about how they cut the white chalk rock there to make my grandma's flower beds. It was a revelation to me. I had always loved the raised round flower beds in the front yard and I always loved the broken up glass on the ridge but I had never put two and two together. Then Bob took me up high to look down on the farm. He asked me if I would like to take care of a farm for my remaining years. I said it was a bit old to do that. He waited for me to answer. I said "Sure." It seemed and still seems a strange idea. We left it there, said goodbye and separated.</p>
      <p>Not what I expected. Just a chatty visit with someone I had not seen for some time. I still don't know what to think of his question. Different members of my family have been showing up. We were never an overtly affectionate bunch. All three sessions have seemed to convey a rather amused and affectionate attitude towards me. I have felt very much at home with them, always felt surprised at what transpires and left wondering at them in a good way.</p>
    </div>
    <div class="col" style="left:262px;top:250px;width:222px">
      <h2>Details about Guided Reunion Sessions</h2>
      <p>More information about the Guided Reunion Sessions procedure at this link: Guided Reunion Sessions</p>
      <h2 style="margin-top:22px">Project Results</h2>
      <ul class="checks">
        <li><svg viewBox="0 0 14 14"><circle cx="7" cy="7" r="7" fill="var(--navy)"/><path d="M4 7.2l2 2 4-4.4" fill="none" stroke="#fff" stroke-width="1.6"/></svg>Validation of the method as a highly effective method of reducing grief</li>
        <li><svg viewBox="0 0 14 14"><circle cx="7" cy="7" r="7" fill="var(--navy)"/><path d="M4 7.2l2 2 4-4.4" fill="none" stroke="#fff" stroke-width="1.6"/></svg>Comparison of the method with conventional grief therapy</li>
      </ul>
      <div class="timeline" style="margin-top:22px">Timeline- 12 months</div>
      <table class="costs">
        <caption>Costs</caption>
        <tr><td>Mediums for validation</td><td>5</td></tr>
        <tr><td>Sessions per medium</td><td>5</td></tr>
        <tr><td>Total sessions</td><td>25</td></tr>
        <tr><td>Cost/session</td><td>$300.00</td></tr>
        <tr><td>Total medium costs</td><td>$7,500.00</td></tr>
        <tr><td>Statistician</td><td>$2,000.00</td></tr>
        <tr><td>Project management</td><td>$3,000.00</td></tr>
        <tr><td>Report design and printing</td><td>$3,000.00</td></tr>
        <tr class="total"><td>PROJECT TOTAL</td><td>$15,500.00</td></tr>
      </table>
    </div>
  </article>
</section>

</body>
</html>
```